Velmora Builders LLC- Bus. Cards, Door Hangers, Invoice, Estimates, Postcards
I want a proffessional package that express who we are and what we do. www.velmora-builders.example
Velmora Builders LLC- Bus. Cards, Door Hangers, Invoice, Estimates, Postcards - Construction
Creative Brief
Professional
Calvin Tressel
Owner
4216 Pellham Ave. Denver, CO. 80417
calvin@velmora-builders.example
www.velmora-builders.example
Spray Foam Insulation Energy Auditing Weatherization Thermal Imaging

```html
<!DOCTYPE html>
<html lang="en">
<head>
<meta charset="utf-8">
<title>Velmora Builders — Stationery Package</title>
<link href="https://fonts.googleapis.com/css2?family=Open+Sans:wght@400;600;700&display=swap" rel="stylesheet">
<style>
:root{
  --green:#7bb83a;
  --green-dark:#5f9a25;
  --green-light:#dcecc8;
  --green-pale:#eef6e4;
  --ink:#3d3d3d;
  --grey:#9a9a9a;
  --line:#cfcfcf;
  --sky-top:#3f86cf;
  --sky-bottom:#a9d2f2;
  --paper:#ffffff;
  --bg:#ffffff;
}
*{box-sizing:border-box;margin:0;padding:0}
html,body{width:1200px;height:362px;overflow:hidden;background:var(--bg)}
body{font-family:"Open Sans",Arial,sans-serif;color:var(--ink);position:relative}
.piece{position:absolute;background:var(--paper);border:1px solid var(--line)}
.caption{position:absolute;font-size:17px;color:#222;text-align:center}
.brand{color:var(--green);font-weight:700;white-space:nowrap;display:flex;align-items:center;gap:4px}
.brand .dot{width:.9em;height:.9em;border-radius:50%;background:var(--green);display:inline-block;flex:none}
.fine{font-size:5px;color:var(--grey);line-height:1.4}

/* postcard */
.postcard-back{left:7px;top:10px;width:142px;height:100px}
.postcard-back .stamp{position:absolute;right:8px;top:8px;width:18px;height:22px;border:1px dashed var(--grey)}
.postcard-back .addr-line{position:absolute;left:72px;width:58px;height:1px;background:var(--line)}
.postcard-back .divider{position:absolute;left:66px;top:10px;width:1px;height:78px;background:var(--line)}
.postcard-back .services{position:absolute;left:8px;top:10px;width:54px;font-size:6px;color:var(--ink);line-height:1.4}
.postcard-front{left:7px;top:106px;width:142px;height:124px;background:var(--paper)}
.postcard-front .mark{position:absolute;left:8px;top:12px;width:30px;height:30px;border-radius:50%;background:var(--green)}
.postcard-front .brand{position:absolute;left:8px;top:50px;font-size:11px}
.postcard-front .band{position:absolute;left:0;right:0;bottom:0;height:44px;background:linear-gradient(var(--green-light),var(--green))}

/* invoice & estimate */
.form{width:234px;height:328px;top:7px}
.invoice{left:168px}
.estimate{left:421px}
.form .brand{position:absolute;left:10px;top:14px;font-size:11px}
.form .title{position:absolute;right:12px;top:10px;font-size:12px;letter-spacing:1px;color:var(--ink)}
.form .meta{position:absolute;right:12px;top:30px;width:70px}
.form .meta div{height:9px;border-bottom:1px solid var(--line)}
.form .bill{position:absolute;left:10px;top:44px;width:100px}
.form .bill div{height:9px;border-bottom:1px solid var(--line)}
.form .bar{position:absolute;left:10px;right:10px;top:78px;height:10px;background:var(--green);color:#fff;font-size:5px;display:flex;align-items:center;padding-left:6px;font-weight:600}
.form .table{position:absolute;left:10px;right:10px;top:92px;height:178px;border:1px solid var(--line);
  background:repeating-linear-gradient(var(--green-pale) 0 9px,var(--paper) 9px 18px)}
.form .table .head{height:10px;background:var(--green-light);display:flex;font-size:5px;font-weight:600;align-items:center}
.form .table .head span{padding-left:4px}
.form .col{position:absolute;top:0;bottom:0;width:1px;background:var(--line)}
.form .totals{position:absolute;right:10px;top:272px;width:66px}
.form .totals div{height:9px;border:1px solid var(--line);border-top:none;font-size:5px;padding-left:3px;line-height:8px}
.form .footer{position:absolute;left:0;right:0;bottom:0;height:22px;background:var(--green);color:#fff;font-size:5px;text-align:center;padding-top:5px;line-height:1.4}
.form .leaf{position:absolute;right:14px;top:130px;width:60px;height:60px;border-radius:50%;background:var(--green);opacity:.08}

/* door hanger */
.door-hanger{left:682px;top:12px;width:98px;height:319px;overflow:hidden;border:none}
.door-hanger .sky{position:absolute;left:0;right:0;top:0;height:105px;background:linear-gradient(var(--sky-top),var(--sky-bottom))}
.door-hanger .hole{position:absolute;left:22px;top:16px;width:38px;height:38px;border-radius:50%;background:var(--paper)}
.door-hanger .services{position:absolute;left:4px;right:4px;top:128px;text-align:center;font-size:8px;line-height:1.35;color:var(--ink)}
.door-hanger .hill{position:absolute;left:0;right:0;bottom:0;height:118px}
.door-hanger .brand{position:absolute;left:7px;top:236px;font-size:8px;color:#fff;gap:3px}
.door-hanger .brand .dot{background:#fff}
.door-hanger .contact{position:absolute;left:7px;top:252px;width:88px;color:#fff;white-space:nowrap;font-size:4.5px}

/* business cards */
.card{width:86px;height:50px;overflow:hidden}
.card-back{left:804px;top:60px;background:linear-gradient(135deg,var(--green),var(--green-dark));border:none}
.card-back .brand{position:absolute;left:8px;top:19px;font-size:8px;color:#fff}
.card-back .brand .dot{background:#fff}
.card-front{left:893px;top:60px}
.card-front .brand,.card-single .brand{position:absolute;left:6px;top:5px;font-size:7px}
.card .who{position:absolute;left:6px;top:17px;font-size:4.5px;color:var(--ink);line-height:1.25;white-space:nowrap}
.card .who span{display:block}
.card .strip{position:absolute;left:0;right:0;bottom:0;height:4px;background:var(--green)}
.card-single{left:870px;top:168px}
.card-label{position:absolute;font-size:7px;color:var(--grey)}

/* envelope */
.envelope{left:996px;top:77px;width:199px;height:132px}
.envelope .brand{position:absolute;left:10px;top:12px;font-size:10px}
.envelope .return{position:absolute;left:10px;top:28px;width:80px}
.envelope .window{position:absolute;left:60px;top:62px;width:80px;height:30px;border:1px solid var(--line);border-radius:3px}
.envelope .band{position:absolute;left:0;right:0;bottom:0;height:18px;background:linear-gradient(90deg,var(--green-light),var(--green))}
.envelope .leaf{position:absolute;right:16px;top:14px;width:44px;height:44px;border-radius:50%;background:var(--green);opacity:.12}
</style>
</head>
<body>

<!-- Postcard -->
<section class="piece postcard-back">
  <p class="services">Spray Foam Insulation<br>Energy Auditing<br>Weatherization<br>Thermal Imaging</p>
  <div class="divider"></div>
  <div class="stamp"></div>
  <div class="addr-line" style="top:48px"></div>
  <div class="addr-line" style="top:60px"></div>
  <div class="addr-line" style="top:72px"></div>
</section>
<section class="piece postcard-front">
  <div class="mark"></div>
  <div class="brand">Velmora Builders</div>
  <div class="band"></div>
</section>
<div class="caption" style="left:7px;top:255px;width:142px">Postcard</div>

<!-- Invoice -->
<section class="piece form invoice">
  <div class="brand"><span class="dot"></span>Velmora Builders</div>
  <div class="title">INVOICE</div>
  <div class="meta"><div class="fine">Date</div><div class="fine">Invoice No.</div></div>
  <div class="bill"><div class="fine">Bill To</div><div></div><div></div></div>
  <div class="bar">Customer Details</div>
  <div class="leaf"></div>
  <div class="table">
    <div class="head"><span style="width:24px">Qty</span><span style="width:120px">Description</span><span style="width:34px">Price</span><span>Amount</span></div>
    <div class="col" style="left:24px"></div><div class="col" style="left:144px"></div><div class="col" style="left:178px"></div>
  </div>
  <div class="totals"><div style="border-top:1px solid var(--line)">Subtotal</div><div>Tax</div><div>Total</div></div>
  <div class="footer">4216 Pellham Ave. Denver, CO. 80417<br>www.velmora-builders.example</div>
</section>
<div class="caption" style="left:168px;top:340px;width:234px">Invoice</div>

<!-- Estimate -->
<section class="piece form estimate">
  <div class="brand"><span class="dot"></span>Velmora Builders</div>
  <div class="title">ESTIMATE</div>
  <div class="meta"><div class="fine">Date</div><div class="fine">Estimate No.</div></div>
  <div class="bill"><div class="fine">Prepared For</div><div></div><div></div></div>
  <div class="bar">Project Information</div>
  <div class="leaf"></div>
  <div class="table">
    <div class="head"><span style="width:24px">Qty</span><span style="width:120px">Description</span><span style="width:34px">Rate</span><span>Amount</span></div>
    <div class="col" style="left:24px"></div><div class="col" style="left:144px"></div><div class="col" style="left:178px"></div>
  </div>
  <div class="totals"><div style="border-top:1px solid var(--line)">Subtotal</div><div>Tax</div><div>Total</div></div>
  <div class="footer">4216 Pellham Ave. Denver, CO. 80417<br>www.velmora-builders.example</div>
</section>
<div class="caption" style="left:421px;top:340px;width:234px">Estimate</div>

<!-- Door hanger -->
<section class="piece door-hanger">
  <div class="sky" role="img" aria-label="Blue sky with soft white clouds"></div>
  <div class="hole"></div>
  <p class="services">Spray Foam Insulation<br>Energy Auditing<br>Weatherization<br>Thermal Imaging</p>
  <svg class="hill" viewBox="0 0 98 118" preserveAspectRatio="none" role="img" aria-label="Rolling green hill">
    <defs><linearGradient id="hillFill" x1="0" y1="0" x2="0" y2="1"><stop offset="0" stop-color="#a8d46f"/><stop offset="1" stop-color="#6aa82e"/></linearGradient></defs>
    <path d="M0 30 Q40 0 98 22 L98 118 L0 118 Z" fill="url(#hillFill)"/>
  </svg>
  <div class="brand"><span class="dot"></span>Velmora Builders</div>
  <div class="contact fine">4216 Pellham Ave.<br>Denver, CO. 80417<br>www.velmora-builders.example</div>
</section>
<div class="caption" style="left:672px;top:340px;width:118px">Door hanger</div>

<!-- Business cards -->
<div class="card-label" style="left:893px;top:114px">Double sided</div>
<section class="piece card card-back"><div class="brand"><span class="dot"></span>Velmora Builders</div></section>
<section class="piece card card-front">
  <div class="brand">Velmora Builders</div>
  <p class="who"><span><b>Calvin Tressel</b>, Owner</span><span>4216 Pellham Ave.</span><span>Denver, CO. 80417</span><span>calvin@velmora-builders.example</span></p>
  <div class="strip"></div>
</section>
<div class="card-label" style="left:870px;top:222px">Single sided</div>
<section class="piece card card-single">
  <div class="brand">Velmora Builders</div>
  <p class="who"><span><b>Calvin Tressel</b>, Owner</span><span>4216 Pellham Ave.</span><span>Denver, CO. 80417</span><span>www.velmora-builders.example</span></p>
  <div class="strip"></div>
</section>
<div class="caption" style="left:804px;top:312px;width:176px">Business cards</div>

<!-- Envelope -->
<section class="piece envelope">
  <div class="brand"><span class="dot"></span>Velmora Builders</div>
  <p class="return fine">4216 Pellham Ave.<br>Denver, CO. 80417</p>
  <div class="leaf"></div>
  <div class="window"></div>
  <div class="band"></div>
</section>
<div class="caption" style="left:996px;top:240px;width:199px">Envelope</div>

</body>
</html>
```